To revamp the exting web page and Company presentation to new propsective client

We are company establish in 2006. We have a combine of Veltrix implementation team of more than 10 years. We focus on the following areas

a) Veltrix T-ledger range implementation
b) Veltrix T-ledger range platform migration
c) Large database size in excess of 20TB

We need to redesign a our existing new card to give a new look and refresh look. Kindly visit our website for more info www.bnlzq.com

Your main them is blue color and hope to hear from you all.

Target Market(s)

Professional clients

Industry/Entity Type

Information Technology

Contact Information for Business Card

To market our as the leading Veltrix partner in Veltrix t-ledger range implementation

Number of Pages Required

1 page

Colors
3276b5
9bcb3c
cadf82
33a6d7

Requirements
Must have
• The ability to attract new customer and show a level of professionalism.
• You can also add a green color to represent green and environmental friendly.
Nice to have
• To give a total new fresh look for the company
Should not have
• None

```html
<!DOCTYPE html>
<html lang="en">
<head>
<meta charset="utf-8">
<title>Nexora Systems – Business Card</title>
<link href="https://fonts.googleapis.com/css2?family=Roboto:wght@400;500;700&family=Roboto+Condensed:wght@400;500&display=swap" rel="stylesheet">
<style>
  :root {
    --bg: #ecebe8;
    --card-white: #ffffff;
    --navy: #14123d;
    --brand-blue: #3a80c4;
    --name-blue: #3276b5;
    --ink: #3d3d3d;
    --ink-soft: #555555;
    --pin-purple: #2b1f5c;
    --badge-red: #d5202a;
    --white: #ffffff;
  }
  * { box-sizing: border-box; margin: 0; padding: 0; }
  html, body { width: 1200px; height: 1000px; overflow: hidden; }
  body { background: var(--bg); font-family: "Roboto", Arial, sans-serif; position: relative; }

  .card {
    position: absolute;
    width: 460px;
    height: 264px;
    border-radius: 6px;
    overflow: hidden;
    box-shadow: 0 6px 18px rgba(0,0,0,.18);
  }

  /* Front */
  .card--front { left: 150px; top: 190px; background: var(--card-white); }
  .brand-lockup {
    position: absolute; left: 34px; top: 96px;
    display: flex; align-items: center; gap: 10px;
  }
  .brand-dot { width: 30px; height: 30px; border-radius: 50%; background: var(--navy); }
  .brand-name {
    font-family: "Roboto", Arial, sans-serif; font-weight: 700;
    font-size: 26px; letter-spacing: 3px; color: var(--navy);
  }
  .divider {
    position: absolute; left: 232px; top: 34px; width: 1px; height: 150px;
    background: #8a8a8a;
  }
  .contact { position: absolute; left: 250px; top: 30px; }
  .person-name { font-size: 22px; font-weight: 700; line-height: 1; }
  .person-name .first { color: var(--name-blue); }
  .person-name .last { color: var(--ink); }
  .person-title {
    font-family: "Roboto Condensed", Arial, sans-serif;
    font-size: 12px; color: var(--ink); margin-top: 4px; letter-spacing: .3px;
  }
  .contact-list { list-style: none; margin-top: 10px; }
  .contact-list li {
    display: flex; align-items: flex-start; gap: 7px;
    font-family: "Roboto Condensed", Arial, sans-serif;
    font-size: 12px; color: var(--ink-soft); line-height: 14px; margin-bottom: 3px;
  }
  .contact-list svg { width: 11px; height: 11px; margin-top: 2px; flex: none; fill: var(--brand-blue); }
  .address-band {
    position: absolute; left: 0; right: 0; top: 202px; height: 44px;
    background: var(--brand-blue); display: flex; align-items: center;
  }
  .pin-box {
    width: 44px; height: 44px; background: var(--pin-purple);
    display: flex; align-items: center; justify-content: center;
  }
  .pin-box svg { width: 20px; height: 20px; }
  .address {
    font-family: "Roboto Condensed", Arial, sans-serif;
    font-size: 11.5px; color: var(--white); line-height: 14px;
    padding-left: 14px; text-align: center; flex: 1; padding-right: 20px;
  }

  /* Back */
  .card--back { left: 590px; top: 540px; background: var(--navy); border-radius: 2px; }
  .partner-badge {
    position: absolute; right: 40px; top: 20px; width: 58px; height: 18px;
    background: var(--badge-red);
  }
  .back-lockup {
    position: absolute; left: 56px; top: 112px;
    display: flex; align-items: center; gap: 10px;
  }
  .back-lockup .brand-dot { background: var(--white); width: 34px; height: 34px; }
  .back-lockup .brand-name { color: var(--white); font-size: 26px; }
  .services {
    position: absolute; left: 246px; top: 84px; list-style: none;
  }
  .services li {
    font-family: "Roboto", Arial, sans-serif; font-size: 15px; color: var(--white);
    line-height: 24px; position: relative; padding-left: 18px;
  }
  .services li::before {
    content: ""; position: absolute; left: 0; top: 9px;
    width: 7px; height: 7px; border-radius: 50%; background: var(--white);
  }
</style>
</head>
<body>

<section class="card card--front" aria-label="Business card front">
  <div class="brand-lockup">
    <span class="brand-dot"></span>
    <span class="brand-name">NEXORA</span>
  </div>
  <div class="divider"></div>
  <div class="contact">
    <h1 class="person-name"><span class="first">KELVIN</span> <span class="last">OOI</span></h1>
    <p class="person-title">CHIEF OPERATING OFFICER</p>
    <ul class="contact-list">
      <li>
        <svg viewBox="0 0 12 12"><path d="M3 0h6a1 1 0 0 1 1 1v10a1 1 0 0 1-1 1H3a1 1 0 0 1-1-1V1a1 1 0 0 1 1-1zm0 1.5v8h6v-8z"/></svg>
        <span>60 12 481 5530<br>60 3 5510 7310</span>
      </li>
      <li>
        <svg viewBox="0 0 12 12"><path d="M1 5c0-2 2-3 5-3s5 1 5 3l-2 1-1-1.5H4L3 6zM2 7h8v4H2z"/></svg>
        <span>65 4092 6617 (Singapore)</span>
      </li>
      <li>
        <svg viewBox="0 0 12 12"><path d="M3 1h6v3H3zM1 5h10v5H9v1H3v-1H1zm3 3v2h4V8z"/></svg>
        <span>60 3 5510 7302</span>
      </li>
      <li>
        <svg viewBox="0 0 12 12"><path d="M0 2h12v8H0zm1 1v.5l5 3 5-3V3z"/></svg>
        <span>kelvinooi@bnlzq.com</span>
      </li>
    </ul>
  </div>
  <div class="address-band">
    <div class="pin-box">
      <svg viewBox="0 0 20 20"><path d="M10 1a6 6 0 0 0-6 6c0 4.5 6 12 6 12s6-7.5 6-12a6 6 0 0 0-6-6zm0 8.5A2.5 2.5 0 1 1 10 4.5a2.5 2.5 0 0 1 0 5z" fill="#ffffff"/></svg>
    </div>
    <p class="address">Suite 12.05, 12th floor, Menara Lumen, Harbour Park, Jalan Teras Biru<br>58100 Kuala Lumpur, Malaysia</p>
  </div>
</section>

<section class="card card--back" aria-label="Business card back">
  <div class="partner-badge" role="img" aria-label="Partner badge"></div>
  <div class="back-lockup">
    <span class="brand-dot"></span>
    <span class="brand-name">NEXORA</span>
  </div>
  <ul class="services">
    <li>Database</li>
    <li>T-Ledger Range</li>
    <li>Consulting</li>
    <li>Support</li>
  </ul>
</section>

</body>
</html>
```